Business Advisory Firm Business Card

A clean, very upscale looking business card. Not crowded.

Please include logo (attached) and:

Daria K. Pellworth
Four Marlow Court
New York, NY 10023
tel: (917) 555-0143
fax: (646) 555-0172
email: dpellworth@quarrystoneconsultants.example
website: www.quarrystoneconsultants.example

Target Market(s)

Business clients. Often real estate development firms, other advisory firms or growing companies that need assistance. I would like a card that looks impressive and confident.

Industry/Entity Type

Business

Colors

Designer to choose colors to be used in the design.

Requirements
Must have
• Impressive and confident. Please include logo.
Should not have
• nothing flashy...

```html
<!DOCTYPE html>
<html lang="en">
<head>
<meta charset="utf-8">
<title>Quarrystone Advisory Services – Business Card</title>
<link rel="stylesheet" href="https://fonts.googleapis.com/css2?family=Arimo:wght@400;700&display=swap">
<style>
  :root {
    --page-bg: #e8eef0;
    --card-white: #ffffff;
    --card-lime: #bdf31f;
    --swoosh-grey: #d3d9dc;
    --ink-dark: #2b3a3d;
    --ink-white: #ffffff;
    --mark-grey: #9aa5a8;
  }
  * { box-sizing: border-box; margin: 0; padding: 0; }
  html, body {
    width: 1200px;
    height: 1000px;
    overflow: hidden;
    background: var(--page-bg);
    font-family: "Arimo", Arial, sans-serif;
  }
  .card {
    position: absolute;
    left: 58px;
    top: 181px;
    width: 1085px;
    height: 636px;
    background: var(--card-white);
    overflow: hidden;
  }
  .card__backdrop {
    position: absolute;
    inset: 0;
  }
  .brand {
    position: absolute;
    left: 103px;
    top: 92px;
    display: flex;
    align-items: center;
    gap: 42px;
  }
  .brand__square {
    width: 160px;
    height: 160px;
    background: var(--mark-grey);
  }
  .brand__name {
    color: var(--ink-dark);
    font-weight: 400;
    font-size: 44px;
    line-height: 1.02;
    letter-spacing: 1px;
  }
  .contact {
    position: absolute;
    left: 339px;
    top: 384px;
    color: var(--ink-dark);
  }
  .contact__name {
    color: var(--ink-white);
    font-weight: 700;
    font-size: 56px;
    line-height: 1;
    margin-bottom: 14px;
  }
  .contact__line { line-height: 1.3; }
  .contact__line--address,
  .contact__line--phone { font-size: 28px; }
  .contact__line--web { font-size: 23.5px; }
  .contact__dot {
    display: inline-block;
    width: 9px;
    height: 9px;
    border-radius: 50%;
    background: var(--ink-dark);
    vertical-align: middle;
    margin: 0 4px 0 2px;
  }
</style>
</head>
<body>
  <article class="card">
    <svg class="card__backdrop" width="1085" height="636" viewBox="0 0 1085 636" aria-hidden="true">
      <path class="card__swoosh" fill="#d3d9dc"
            d="M0,346 C700,336 1010,250 1045,0 L1085,0 C1075,210 860,332 0,346 Z"/>
      <path class="card__band" fill="#bdf31f"
            d="M0,347 C820,336 1065,230 1085,40 L1085,636 L0,636 Z"/>
    </svg>

    <div class="brand">
      <div class="brand__square"></div>
      <div class="brand__name">Quarrystone<br>Advisory<br>Services, Inc.</div>
    </div>

    <div class="contact">
      <h1 class="contact__name">Daria K. Pellworth</h1>
      <p class="contact__line contact__line--address">Four Marlow Court, New York, NY 10023</p>
      <p class="contact__line contact__line--phone">tel: (917) 555-0143<span class="contact__dot"></span>fax: (646) 555-0172</p>
      <p class="contact__line contact__line--web">email: dpellworth@quarrystoneconsultants.example</p>
      <p class="contact__line contact__line--web">website: www.quarrystoneconsultants.example</p>
    </div>
  </article>
</body>
</html>
```